Mobile phone signal boosting solutions needs a website

We need a website design for the reselling of a mobile signal boosting product set. These solutions are Vexlor exempt and will provide an indoor signal for mobile phones. We would like to see designs that incorporate the colours and feel of our logo. The domain will be
openmeadow.com / co.uk
Overview of the company and how it is to be used: Open meadow (domain name) will work with business and end user to provide mobile signal boosting – where people struggle indoors with a mobile signal our solutions will help by finding the smallest signal and boosting it, allowing users to use voice and data over their mobile network (please note this is not wireless signal boosting)
Number of Pages:
-Home
-Solutions / How it works
-Case Studies
-Contact
Text content: Currently just use placeholders
Technical specs : Wordpress and ability to use CMS if that’s relevant
Target Market(s)
Business professional all markets /high end residential
Coded - Design and coding required
4 page

```html
<!DOCTYPE html>
<html lang="en">
<head>
<meta charset="utf-8">
<title>Open meadow – Mobile Signal Booster</title>
<link rel="stylesheet" href="https://fonts.googleapis.com/css2?family=Roboto:wght@400;500;700;900&display=swap">
<style>
  :root {
    --yellow: #fcbd17;
    --amber: #f9a71c;
    --orange: #f8981d;
    --ink: #111111;
    --body: #6b6b6b;
    --white: #ffffff;
    --dark: #24252a;
    --blue-deep: #0b3a8c;
    --blue-light: #17a4d8;
  }
  * { margin: 0; padding: 0; box-sizing: border-box; }
  html, body { width: 1200px; height: 3604px; overflow: hidden; }
  body { position: relative; font-family: "Roboto", sans-serif; background: var(--white); color: var(--ink); }
  .abs { position: absolute; }

  .top-rule { left: 0; top: 0; width: 1200px; height: 4px; background: var(--yellow); }
  .site-header { left: 0; top: 4px; width: 1200px; height: 118px; background: var(--white); }
  .brand-tab { left: 112px; top: 118px; width: 224px; height: 64px; z-index: 3; }
  .brand { left: 112px; top: 114px; width: 224px; text-align: center; z-index: 4; }
  .brand-name { font-size: 28px; font-weight: 500; color: var(--ink); letter-spacing: -0.5px; line-height: 1; }
  .brand-tag { font-size: 11px; font-weight: 500; color: var(--yellow); margin-top: 4px; }

  .btn { display: flex; align-items: center; justify-content: center; font-weight: 500; font-size: 15px; color: var(--ink); }
  .btn-yellow { background: var(--yellow); }
  .btn-white { background: var(--white); }
  .header-cta { left: 934px; top: 24px; width: 154px; height: 42px; }

  .main-nav { top: 83px; right: 112px; display: flex; gap: 35px; font-size: 15px; color: #222; }

  .hero { left: 0; top: 122px; width: 1200px; height: 506px;
    background: linear-gradient(100deg, #fdb81a 0%, #fcbd1d 45%, #f9a11c 100%); }
  .hero-visual { left: 630px; top: 133px; width: 530px; height: 495px;
    background: linear-gradient(180deg, rgba(14,52,130,0.85) 0%, rgba(30,110,200,0.55) 65%, rgba(249,161,28,0) 100%); }
  .hero-title { left: 109px; top: 262px; font-size: 63px; font-weight: 900; line-height: 1.05; color: var(--ink); }
  .hero-text { left: 112px; top: 404px; width: 420px; font-size: 15.5px; line-height: 27px; color: #222; }
  .hero-cta { left: 112px; top: 503px; width: 127px; height: 42px; }

  .frame { border: 4px solid var(--yellow); }
  .photo { border-radius: 6px; }
  .about-frame { left: 95px; top: 726px; width: 272px; height: 294px; }
  .about-photo { left: 131px; top: 762px; width: 430px; height: 465px;
    background: linear-gradient(160deg, #3f7fc9 0%, #6ea6dd 55%, #b7d4ef 100%); }
  .section-title { font-size: 42px; font-weight: 700; color: var(--ink); }
  .about-title { left: 615px; top: 786px; }
  .copy { font-size: 13.5px; line-height: 27.4px; color: var(--body); width: 470px; }
  .about-copy1 { left: 615px; top: 851px; }
  .about-copy2 { left: 615px; top: 1043px; }
  .about-cta { left: 615px; top: 1148px; width: 130px; height: 42px; }

  .solutions-title { left: 130px; top: 1356px; }
  .solutions-copy { left: 130px; top: 1418px; width: 470px; }
  .solution-list { left: 130px; top: 1548px; list-style: none; font-size: 13.5px; color: var(--body); }
  .solution-list li { display: flex; align-items: center; gap: 17px; height: 33px; }
  .solutions-cta { left: 130px; top: 1709px; width: 130px; height: 42px; }
  .solutions-frame { left: 836px; top: 1291px; width: 274px; height: 294px; }
  .solutions-photo { left: 641px; top: 1327px; width: 430px; height: 465px;
    background: radial-gradient(circle at 50% 45%, #4fc3f0 0%, #1a6fc2 40%, #0b3a8c 100%); }

  .cases-band { left: 0; top: 1911px; width: 1200px; height: 770px; }
  .cases-title { left: 0; top: 1976px; width: 1200px; text-align: center; font-size: 42px; font-weight: 700; color: var(--white); }
  .case-card { top: 2062px; width: 309px; height: 408px; background: var(--white); text-align: center; }
  .case-photo { margin: 11px 10px 0; height: 200px; }
  .case-title { margin-top: 24px; font-size: 17px; font-weight: 500; line-height: 26px; color: #222; }
  .case-text { margin: 10px auto 0; width: 250px; font-size: 12.5px; line-height: 20px; color: var(--body); }
  .case-link { display: inline-block; margin-top: 10px; font-size: 14px; font-weight: 700; color: var(--yellow); text-decoration: underline; }
  .cases-cta { left: 537px; top: 2508px; width: 127px; height: 42px; }

  .contact-title { left: 0; top: 2722px; width: 1200px; text-align: center; }
  .field { left: 112px; width: 471px; height: 64px; background: var(--white); border-radius: 8px;
    box-shadow: 0 2px 14px rgba(0,0,0,0.10); font-size: 13px; color: #666; padding: 26px 42px; }
  .message { left: 617px; top: 2807px; width: 473px; height: 331px; }
  .submit { left: 112px; top: 3074px; width: 471px; height: 64px; border-radius: 8px; font-size: 13px; font-weight: 700;
    background: linear-gradient(180deg, #fcc21f, #f9ad1a); }

  .site-footer { left: 0; top: 3236px; width: 1200px; height: 368px; background: var(--dark); }
  .footer-brand { left: 0; top: 3410px; width: 1200px; text-align: center; color: var(--white); }
  .footer-brand .brand-name { color: var(--white); font-size: 42px; }
  .footer-brand .brand-tag { color: var(--white); font-size: 18px; margin-top: 6px; }
  .footer-nav { top: 3512px; font-size: 15px; color: var(--white); }
  .copyright { left: 0; top: 3556px; width: 1200px; text-align: center; font-size: 14.5px; color: var(--white); }
</style>
</head>
<body>
  <div class="abs top-rule"></div>
  <header class="abs site-header"></header>
  <svg class="abs brand-tab" viewBox="0 0 224 64" aria-hidden="true"><polygon points="0,0 224,0 196,64 28,64" fill="#fff"/></svg>
  <div class="abs brand">
    <div class="brand-name">Open meadow</div>
    <div class="brand-tag">MOBILE SIGNAL BOOSTER</div>
  </div>
  <a class="abs btn btn-yellow header-cta">Get Started</a>
  <nav class="abs main-nav"><span>Home</span><span>Solutions/How It Works</span><span>Case Studies</span><span>Contact Us</span></nav>

  <section class="abs hero"></section>
  <div class="abs hero-visual" role="img" aria-label="City skyline at night seen through rising signal bars"></div>
  <h1 class="abs hero-title">MOBILE SIGNAL<br>BOOSTER</h1>
  <p class="abs hero-text">Lorem Ipsum is simply dummy text of the printing and typesetting industry. Lorem Ipsum has been the industry's standard dummy text ever since</p>
  <a class="abs btn btn-white hero-cta">Get Started</a>

  <div class="abs frame about-frame"></div>
  <div class="abs photo about-photo" role="img" aria-label="Telecom mast with antennas against a blue sky and network lines"></div>
  <h2 class="abs section-title about-title">ABOUT US</h2>
  <p class="abs copy about-copy1">Lorem Ipsum is simply dummy text of the printing and typesetting industry. Lorem Ipsum has been the industry's standard dummy text ever since the 1500s, when an unknown printer took a galley of type and scrambled it to make a type specimen book. It has survived not only five centuries, but also the leap into electronic typesetting, remaining essentially unchanged. It was popularised in the 1960s with the release</p>
  <p class="abs copy about-copy2">Lorem Ipsum is simply dummy text of the printing and typesetting industry. Lorem Ipsum has been the industry's standard dummy text ever since the 1500s, when an unknown printer took a galley</p>
  <a class="abs btn btn-yellow about-cta">Read More</a>

  <h2 class="abs section-title solutions-title">OUR SOLUTIONS</h2>
  <p class="abs copy solutions-copy">Lorem Ipsum is simply dummy text of the printing and typesetting industry. Lorem Ipsum has been the industry's standard dummy text ever since the 1500s, when an unknown printer took a galley of type and scrambled it to make a type specimen book.</p>
  <ul class="abs solution-list">
    <li><svg width="36" height="12" viewBox="0 0 36 12" aria-hidden="true"><path d="M0 6H34M28 1L34 6L28 11" stroke="#333" stroke-width="1.6" fill="none"/></svg>Lorem Ipsum is simply dummy text of the printing</li>
    <li><svg width="36" height="12" viewBox="0 0 36 12" aria-hidden="true"><path d="M0 6H34M28 1L34 6L28 11" stroke="#333" stroke-width="1.6" fill="none"/></svg>Lorem Ipsum is simply</li>
    <li><svg width="36" height="12" viewBox="0 0 36 12" aria-hidden="true"><path d="M0 6H34M28 1L34 6L28 11" stroke="#333" stroke-width="1.6" fill="none"/></svg>Lorem Ipsum is simply dummy text</li>
    <li><svg width="36" height="12" viewBox="0 0 36 12" aria-hidden="true"><path d="M0 6H34M28 1L34 6L28 11" stroke="#333" stroke-width="1.6" fill="none"/></svg>Lorem Ipsum of the printing</li>
  </ul>
  <a class="abs btn btn-yellow solutions-cta">Read More</a>
  <div class="abs frame solutions-frame"></div>
  <div class="abs photo solutions-photo" role="img" aria-label="Glowing globe surrounded by connected device icons on a blue background"></div>

  <svg class="abs cases-band" viewBox="0 0 1200 770" preserveAspectRatio="none" aria-hidden="true">
    <defs><linearGradient id="caseBg" x1="0" y1="0" x2="0" y2="1"><stop offset="0" stop-color="#f9a01d"/><stop offset="1" stop-color="#fcbd17"/></linearGradient></defs>
    <path d="M0 0H1200V768C1000 760 800 735 600 715C380 690 200 700 0 754Z" fill="url(#caseBg)"/>
  </svg>
  <h2 class="abs cases-title">CASE STUDIES</h2>
  <article class="abs case-card" style="left:112px">
    <div class="case-photo" role="img" aria-label="Night city skyline with network arcs" style="background:linear-gradient(180deg,#2b4f8f,#0e1f3f)"></div>
    <h3 class="case-title">LOREM IPSUM IS SIMPLY DUMMY<br>TEXT OF THE PRNTING</h3>
    <p class="case-text">Lorem Ipsum is simply dummy text of the printing and typesetting industry. Lorem Ipsum has been the industry's</p>
    <a class="case-link">View More</a>
  </article>
  <article class="abs case-card" style="left:446px">
    <div class="case-photo" role="img" aria-label="Hands using laptops and phones around a table with network icons" style="background:linear-gradient(180deg,#5a4d44,#2f2824)"></div>
    <h3 class="case-title">LOREM IPSUM IS SIMPLY DUMMY<br>TEXT OF THE PRNTING</h3>
    <p class="case-text">Lorem Ipsum is simply dummy text of the printing and typesetting industry. Lorem Ipsum has been the industry's</p>
    <a class="case-link">View More</a>
  </article>
  <article class="abs case-card" style="left:780px">
    <div class="case-photo" role="img" aria-label="Businesswoman working with digital screens" style="background:linear-gradient(90deg,#1c3255,#4a3a35)"></div>
    <h3 class="case-title">LOREM IPSUM IS SIMPLY DUMMY<br>TEXT OF THE PRNTING</h3>
    <p class="case-text">Lorem Ipsum is simply dummy text of the printing and typesetting industry. Lorem Ipsum has been the industry's</p>
    <a class="case-link">View More</a>
  </article>
  <a class="abs btn btn-white cases-cta">Get Started</a>

  <h2 class="abs section-title contact-title">GET IN TOUCH WITH US</h2>
  <div class="abs field" style="top:2807px">Full Name</div>
  <div class="abs field" style="top:2897px">Contact Number</div>
  <div class="abs field" style="top:2986px">Email Address</div>
  <div class="abs field message">Your Message Goes Here...</div>
  <a class="abs btn submit">Submit Here</a>

  <footer class="abs site-footer"></footer>
  <div class="abs footer-brand">
    <div class="brand-name">Open meadow</div>
    <div class="brand-tag">MOBILE SIGNAL BOOSTER</div>
  </div>
  <span class="abs footer-nav" style="left:272px">Home</span>
  <span class="abs footer-nav" style="left:359px">|</span>
  <span class="abs footer-nav" style="left:408px">Solutions/How It Works</span>
  <span class="abs footer-nav" style="left:617px">|</span>
  <span class="abs footer-nav" style="left:667px">Case Studies</span>
  <span class="abs footer-nav" style="left:802px">|</span>
  <span class="abs footer-nav" style="left:852px">Contact Us</span>
  <p class="abs copyright">© Copyright 2023 Open meadow | All Rights Reserved.</p>
</body>
</html>
```